Business Card Design Project

Lumen Clinic Group

Dr Tomas Feldren M.D, F.R.C.S
Vascular and Vein Surgery

18-46 Corbell Avenue, Suite 317
Astoria
NY 11290

212-555-0163
718-555-0147
www.palemedic.example back of the card for scheduled appointments up to 5 appointment dates

Target Market(s)

Male and Female patients from 25 onwards with spider veins or varicose veins

Industry/Entity Type

Business

Font styles to use
Serif

Colors
86cae6
85abd2
0456a4

Requirements
Must have
• Modern Sophisticated design using light blue and grey text
Should not have
• hearts or flowers

```html
<!DOCTYPE html>
<html lang="en">
<head>
<meta charset="utf-8">
<title>Lumen Clinic Group – Business Card</title>
<link rel="stylesheet" href="https://fonts.googleapis.com/css2?family=Lora:wght@400;600;700&display=swap">
<style>
  :root {
    --blue-deep: #0456a4;
    --blue-mid: #85abd2;
    --blue-light: #86cae6;
    --blue-brand: #2f72b5;
    --grey-text: #4a4a4a;
    --grey-dots: #9a9a9a;
    --panel: #f3f4f6;
    --white: #ffffff;
    --backdrop: #e9ecef;
    --skin: #e9c3a6;
    --skin-shade: #d7a586;
    --sheet: #dfe3ea;
  }
  * { box-sizing: border-box; margin: 0; padding: 0; }
  html, body {
    width: 1200px; height: 1023px; overflow: hidden;
    background: var(--backdrop);
    font-family: "Lora", Georgia, serif;
  }
  .canvas { position: relative; width: 1200px; height: 1023px; }

  .card {
    position: absolute; width: 700px; height: 400px;
    border-radius: 6px; overflow: hidden;
    box-shadow: 0 10px 24px rgba(0,0,0,.18);
  }

  /* Back: appointments */
  .card-back {
    left: 150px; top: 70px;
    background: linear-gradient(160deg, #2d7cc6 0%, var(--blue-deep) 70%);
    color: var(--white);
  }
  .card-back .title {
    text-align: center; font-size: 20px; letter-spacing: 1px;
    margin-top: 20px;
  }
  .appointment-panel {
    position: absolute; left: 40px; top: 62px; width: 620px; height: 222px;
    background: linear-gradient(180deg, var(--white), var(--panel));
    border-radius: 12px;
    padding: 22px 30px 0 30px;
  }
  .appointment-row {
    display: flex; gap: 18px; height: 39px; align-items: flex-end;
    color: var(--grey-text); font-size: 14px;
  }
  .appointment-row .field { flex: 1; display: flex; align-items: flex-end; }
  .appointment-row .field .line {
    flex: 1; border-bottom: 1.5px dotted var(--grey-dots);
    margin: 0 0 4px 4px;
  }
  .back-footer {
    position: absolute; left: 40px; right: 40px; bottom: 26px;
    display: flex; align-items: center; font-size: 15px; line-height: 1.45;
  }
  .back-footer .hours { flex: 1; }
  .back-footer .divider {
    width: 1px; height: 52px; background: rgba(255,255,255,.6); margin: 0 22px;
  }
  .back-footer .address { width: 250px; }

  /* Front: contact */
  .card-front {
    left: 350px; top: 560px; background: var(--white);
  }
  .treatment-photo {
    position: absolute; right: 0; top: 0; width: 430px; height: 100%;
    background:
      linear-gradient(90deg, var(--white) 0%, rgba(255,255,255,0) 40%),
      linear-gradient(200deg, var(--skin) 0%, var(--skin-shade) 45%, var(--sheet) 80%);
  }
  .brand {
    position: absolute; left: 40px; top: 46px;
    display: flex; align-items: center; gap: 12px;
  }
  .brand .mark {
    width: 22px; height: 22px; border-radius: 50%; background: var(--blue-brand);
  }
  .brand .name {
    font-size: 34px; font-weight: 700; color: var(--blue-brand);
    line-height: 1;
  }
  .doctor {
    position: absolute; left: 40px; top: 198px;
  }
  .doctor .name { color: var(--blue-brand); font-size: 20px; }
  .doctor .specialty { color: var(--grey-text); font-size: 15px; margin-top: 2px; }
  .contact-list {
    position: absolute; left: 40px; top: 262px; list-style: none;
    color: var(--grey-text); font-size: 17px;
  }
  .contact-list li { display: flex; align-items: center; gap: 10px; height: 26px; }
  .contact-list .icon { width: 18px; height: 18px; }
  .street-address {
    position: absolute; left: 40px; top: 346px;
    color: var(--grey-text); font-size: 14px; line-height: 1.55;
  }
</style>
</head>
<body>
<main class="canvas">

  <section class="card card-back" aria-label="Appointment card, back">
    <h2 class="title">APPOINTMENTS</h2>
    <div class="appointment-panel">
      <div class="appointment-row"><span class="field">Date<span class="line"></span></span><span class="field">Time<span class="line"></span></span></div>
      <div class="appointment-row"><span class="field">Date<span class="line"></span></span><span class="field">Time<span class="line"></span></span></div>
      <div class="appointment-row"><span class="field">Date<span class="line"></span></span><span class="field">Time<span class="line"></span></span></div>
      <div class="appointment-row"><span class="field">Date<span class="line"></span></span><span class="field">Time<span class="line"></span></span></div>
      <div class="appointment-row"><span class="field">Date<span class="line"></span></span><span class="field">Time<span class="line"></span></span></div>
    </div>
    <div class="back-footer">
      <div class="hours">Hours<br>Monday to Saturday - 9:00am to 5:00pm</div>
      <div class="divider"></div>
      <div class="address">18-46 Corbell Avenue, Suite 317<br>Astoria, NY 11290</div>
    </div>
  </section>

  <section class="card card-front" aria-label="Business card, front">
    <div class="treatment-photo" role="img" aria-label="Photo of a laser vein treatment on a patient's leg"></div>

    <div class="brand">
      <span class="mark"></span>
      <span class="name">Lumen Clinic Group</span>
    </div>

    <div class="doctor">
      <p class="name">Dr Tomas Feldren M.D, F.R.C.S</p>
      <p class="specialty">Vascular and Vein Surgery</p>
    </div>

    <ul class="contact-list">
      <li>
        <svg class="icon" viewBox="0 0 18 18" aria-hidden="true"><circle cx="9" cy="9" r="9" fill="var(--blue-deep)"/><path d="M5 7.5c0-1.5 1.8-2.3 4-2.3s4 .8 4 2.3l-1.4.4-.3-1.1H6.7l-.3 1.1zM6.2 8.5h5.6l.8 4H5.4z" fill="#fff"/></svg>
        212-555-0163
      </li>
      <li>
        <svg class="icon" viewBox="0 0 18 18" aria-hidden="true"><circle cx="9" cy="9" r="9" fill="var(--blue-deep)"/><rect x="6" y="3.8" width="6" height="10.4" rx="1.2" fill="#fff"/><rect x="7" y="5" width="4" height="7" fill="var(--blue-deep)"/></svg>
        718-555-0147
      </li>
      <li>
        <svg class="icon" viewBox="0 0 18 18" aria-hidden="true"><circle cx="9" cy="9" r="9" fill="var(--blue-deep)"/><g fill="none" stroke="#fff" stroke-width="1"><circle cx="9" cy="9" r="5"/><ellipse cx="9" cy="9" rx="2.2" ry="5"/><path d="M4 9h10M5 6.5h8M5 11.5h8"/></g></svg>
        www.palemedic.example
      </li>
    </ul>

    <p class="street-address">18-46 Corbell Avenue, Suite 317,<br>Astoria NY 11290</p>
  </section>

</main>
</body>
</html>
```